I need three graphics made that will go on walls in a basketball lockerroom

I need three graphics made that will go on a basketball lockerroom wall. Here are the specifics.
Graphic 1 (Size 115" wide by 52" tall, min 150 DPI)
This should be something that displays the acronym for TOLVAR. The main background color should be the teal color attached. Use logos and the other approved colors as needed.
Standards
Intensity
Effort
Grit
Energy
Love
Graphic 2 (Size 88" wide by 52" tall, min 150 DPI)
This one should be on the Navy Blue background color attached
and impactful way say Attitude and Effort
Graphic 3 (Size 100" wide by 18" tall, min 150 DPI)
This goes along the top of the way and needs to say
(THS logo) Stars Lead the Way (Star logo) Tolvar Basketball (THS logo)
All three of these need to feel like they are of the same style. For Graphic #2 I thought something maybe like the attached basketball except use the S Star in the middle and say attitude and effort using the colors .. but I'm open to other ideas

```html
<!DOCTYPE html>
<html lang="en">
<head>
<meta charset="utf-8">
<title>Tolvar Basketball Locker Room Graphics</title>
<link href="https://fonts.googleapis.com/css2?family=Alfa+Slab+One&family=Oswald:wght@500;600&display=swap" rel="stylesheet">
<style>
:root{
  --page:#bdbdbd;
  --navy:#1b2a55;
  --navy-deep:#111c3d;
  --royal:#1f4aa8;
  --teal:#1aa3a8;
  --teal-dark:#0f7f86;
  --silver-hi:#ffffff;
  --silver-mid:#c9ccd3;
  --silver-lo:#8a8f99;
  --line:#8fd9e0;
}
*{box-sizing:border-box;margin:0;padding:0}
html,body{width:1200px;height:1200px;overflow:hidden;background:var(--page)}
.canvas{position:relative;width:1200px;height:1200px}
.graphic{position:absolute;overflow:hidden;box-shadow:0 6px 14px rgba(0,0,0,.35)}
.graphic svg.frame{position:absolute;inset:0;width:100%;height:100%}
.chrome{
  font-family:"Alfa Slab One",serif;
  background:linear-gradient(180deg,var(--silver-hi) 0%,var(--silver-mid) 45%,var(--silver-lo) 55%,var(--silver-hi) 100%);
  -webkit-background-clip:text;background-clip:text;color:transparent;
  -webkit-text-stroke:1.5px var(--teal);
  text-align:center;line-height:1;
}
.mark-name{position:absolute;font-family:"Alfa Slab One",serif;color:var(--silver-hi);text-align:center;line-height:1}
.caption{position:absolute;font-family:"Oswald",sans-serif;font-weight:500;letter-spacing:.18em;color:var(--navy);line-height:1}
.star-seat{position:absolute;border-radius:50%;background:var(--navy);border:3px solid var(--silver-mid)}

/* Top banner */
.banner{left:100px;top:335px;width:1000px;height:180px;background:radial-gradient(ellipse at center,#24386c 0%,var(--navy) 55%,var(--navy-deep) 100%)}
.banner .mark-name{top:64px;font-size:34px;width:120px}
.banner .title{position:absolute;top:44px;font-size:52px;width:270px}
.banner .sub{position:absolute;top:106px;width:270px;text-align:center;font-family:"Alfa Slab One",serif;font-size:18px;letter-spacing:.1em;color:var(--silver-mid)}

/* Values graphic */
.values{left:20px;top:575px;width:640px;height:290px;background:linear-gradient(180deg,#2a3f75 0%,var(--navy) 60%,var(--navy-deep) 100%)}
.values .bg-photo{position:absolute;left:0;top:0;width:100%;height:220px;background:radial-gradient(ellipse at 30% 60%,rgba(60,90,150,.45),transparent 60%)}
.values .mark-name{left:0;right:0;top:14px;font-size:40px}
.acronym{position:absolute;left:40px;right:40px;top:70px;display:grid;grid-template-columns:repeat(6,1fr)}
.acronym .col{text-align:center;border-left:1px solid rgba(180,200,230,.45);padding-top:4px}
.acronym .col:first-child{border-left:none}
.acronym .letter{font-size:80px;display:block}
.acronym .word{display:block;margin-top:18px;font-family:"Oswald",sans-serif;font-weight:600;font-size:17px;color:#fff;letter-spacing:.02em}

/* Attitude graphic */
.attitude{left:690px;top:575px;width:490px;height:290px;background:linear-gradient(160deg,#2457b8 0%,var(--royal) 40%,#173a86 100%)}
.attitude .bg-photo{position:absolute;right:0;top:0;width:55%;height:210px;background:radial-gradient(ellipse at 70% 40%,rgba(120,170,240,.35),transparent 70%)}
.attitude .player{position:absolute;left:118px;top:50px;width:46px;height:96px;border-radius:10px;background:linear-gradient(180deg,rgba(230,232,238,.35),rgba(154,160,170,.15))}
.attitude .mark-name{left:0;right:0;top:16px;font-size:30px}
.attitude .big{position:absolute;left:0;right:0;font-size:56px}
.attitude .and{position:absolute;left:0;right:0;top:136px;font-size:20px;-webkit-text-stroke:.8px var(--teal-dark)}
</style>
</head>
<body>
<div class="canvas">

  <!-- Graphic 3: top wall banner -->
  <section class="graphic banner" aria-label="Stars Lead the Way banner">
    <svg class="frame" viewBox="0 0 1000 180" preserveAspectRatio="none" aria-hidden="true">
      <polygon points="0,0 130,0 170,150 0,150" fill="#15224a"/>
      <polygon points="1000,0 870,0 830,150 1000,150" fill="#15224a"/>
      <polyline points="105,0 165,150 440,150 470,180" fill="none" stroke="var(--silver-hi)" stroke-width="3"/>
      <polyline points="895,0 835,150 560,150 530,180" fill="none" stroke="var(--silver-hi)" stroke-width="3"/>
      <polygon points="0,150 165,150 170,160 830,160 835,150 1000,150 1000,180 0,180" fill="var(--teal)"/>
      <circle cx="500" cy="85" r="62" fill="none" stroke="rgba(143,217,224,.25)" stroke-width="2"/>
    </svg>
    <div class="mark-name" style="left:4px">THS</div>
    <div class="mark-name" style="right:4px">THS</div>
    <div class="chrome title" style="left:155px">STARS</div>
    <div class="sub" style="left:155px">LEAD THE WAY</div>
    <div class="star-seat" style="left:462px;top:50px;width:76px;height:76px"></div>
    <div class="chrome title" style="left:585px">TOLVAR</div>
    <div class="sub" style="left:585px">BASKETBALL</div>
  </section>

  <!-- Graphic 1: acronym values -->
  <section class="graphic values" aria-label="Tolvar acronym values wall">
    <div class="bg-photo" role="img" aria-label="Faint basketball court and ball photo in navy tones"></div>
    <svg class="frame" viewBox="0 0 640 290" preserveAspectRatio="none" aria-hidden="true">
      <defs>
        <linearGradient id="silverBar" x1="0" x2="1">
          <stop offset="0" stop-color="#9ea3ad"/><stop offset=".5" stop-color="#ffffff"/><stop offset="1" stop-color="#9ea3ad"/>
        </linearGradient>
      </defs>
      <polyline points="20,42 200,42 215,32" fill="none" stroke="var(--line)" stroke-width="1"/>
      <polyline points="620,42 440,42 425,32" fill="none" stroke="var(--line)" stroke-width="1"/>
      <polygon points="0,190 60,235 580,235 640,190 640,290 0,290" fill="var(--teal)"/>
      <polygon points="30,242 610,242 595,262 45,262" fill="url(#silverBar)"/>
      <polygon points="0,268 640,268 640,290 0,290" fill="var(--navy)"/>
    </svg>
    <div class="mark-name">THS</div>
    <div class="acronym">
      <div class="col"><span class="chrome letter">T</span><span class="word">STANDARDS</span></div>
      <div class="col"><span class="chrome letter">O</span><span class="word">INTENSITY</span></div>
      <div class="col"><span class="chrome letter">L</span><span class="word">EFFORT</span></div>
      <div class="col"><span class="chrome letter">V</span><span class="word">GRIT</span></div>
      <div class="col"><span class="chrome letter">A</span><span class="word">ENERGY</span></div>
      <div class="col"><span class="chrome letter">R</span><span class="word">LOVE</span></div>
    </div>
    <div class="caption" style="left:95px;top:244px;font-size:16px">TOGATHER WE RISE</div>
    <div class="caption" style="right:95px;top:244px;font-size:16px">OUR STANDERDS</div>
    <div class="star-seat" style="left:290px;top:222px;width:60px;height:60px"></div>
  </section>

  <!-- Graphic 2: attitude and effort -->
  <section class="graphic attitude" aria-label="Attitude and Effort wall">
    <div class="bg-photo" role="img" aria-label="Faint photo of a player dunking in an arena, blue tones"></div>
    <div class="player" role="img" aria-label="Silver silhouette of a player dribbling"></div>
    <svg class="frame" viewBox="0 0 490 290" preserveAspectRatio="none" aria-hidden="true">
      <defs>
        <linearGradient id="silverBar2" x1="0" x2="1">
          <stop offset="0" stop-color="#9ea3ad"/><stop offset=".5" stop-color="#ffffff"/><stop offset="1" stop-color="#9ea3ad"/>
        </linearGradient>
      </defs>
      <polyline points="10,40 150,40 165,30" fill="none" stroke="var(--line)" stroke-width="1"/>
      <polyline points="480,40 340,40 325,30" fill="none" stroke="var(--line)" stroke-width="1"/>
      <polygon points="0,200 40,240 450,240 490,200 490,290 0,290" fill="var(--teal)"/>
      <polygon points="25,246 465,246 452,264 38,264" fill="url(#silverBar2)"/>
      <polygon points="0,270 490,270 490,290 0,290" fill="var(--navy)"/>
    </svg>
    <div class="mark-name">THS</div>
    <div class="chrome big" style="top:74px">ATTITUDE</div>
    <div class="chrome and">AND</div>
    <div class="chrome big" style="top:162px">EFFORT</div>
    <div class="caption" style="left:60px;top:250px;font-size:13px">TOGATHER WE RISE</div>
    <div class="caption" style="right:60px;top:250px;font-size:13px">OUR STANDERDS</div>
    <div class="star-seat" style="left:219px;top:230px;width:52px;height:52px"></div>
  </section>

</div>
</body>
</html>
```